Sign Design for Truck Repair Shop center

Need a road-side sign for a pickup truck repair shop called HaulPoint Garage. The logo is attached and should be used on the sign. The background should be white and the main part of the logo should take up a large part of the sign so it can be easily read by passing traffic. The sign is 4 feet tall by 8 feet wide. Also need to add the website address" "www.HaulPointGarage-example.com" and "Call/Text 555.382.4607"

```html
<!DOCTYPE html>
<html lang="en">
<head>
<meta charset="utf-8">
<title>HaulPoint Garage – Roadside Sign</title>
<link rel="stylesheet" href="https://fonts.googleapis.com/css2?family=Graduate&family=Michroma&display=swap">
<style>
  :root {
    --page: #ffffff;
    --plate: #ffffff;
    --band-light: #6b5f50;
    --band-dark: #2e2822;
    --rivet: #8a7a62;
    --rivet-edge: #2a241d;
    --ink-light: #ffffff;
    --ink-dark: #1c1a17;
  }
  html, body {
    margin: 0;
    width: 936px;
    height: 1200px;
    overflow: hidden;
    background: var(--page);
  }
  .sign {
    position: absolute;
    left: 36px;
    top: 384px;
    width: 864px;
    height: 432px;
    background: var(--plate);
    box-shadow: 6px 8px 16px rgba(0,0,0,0.35);
    outline: 1px solid #d8d4ce;
    overflow: hidden;
  }
  .sign__bands {
    position: absolute;
    inset: 0;
  }
  .sign__phone {
    position: absolute;
    top: 22px;
    left: 0;
    right: 0;
    display: flex;
    justify-content: center;
    gap: 42px;
    font-family: "Graduate", serif;
    font-size: 50px;
    line-height: 1;
    color: var(--ink-light);
  }
  .sign__brand {
    position: absolute;
    top: 158px;
    left: 0;
    right: 0;
    text-align: center;
    color: var(--ink-dark);
    font-family: "Graduate", serif;
  }
  .sign__name {
    font-size: 74px;
    line-height: 1;
    margin: 0;
    white-space: nowrap;
  }
  .sign__tagline {
    font-size: 22px;
    letter-spacing: 1px;
    line-height: 1;
    margin: 22px 0 0;
  }
  .sign__web {
    position: absolute;
    top: 372px;
    left: 0;
    right: 0;
    text-align: center;
    font-family: "Michroma", sans-serif;
    font-size: 21px;
    letter-spacing: 3px;
    color: var(--ink-light);
  }
</style>
</head>
<body>
  <div class="sign">
    <svg class="sign__bands" width="864" height="432" viewBox="0 0 864 432" aria-hidden="true">
      <defs>
        <linearGradient id="band-top" x1="0" y1="0" x2="0" y2="1">
          <stop offset="0" stop-color="var(--band-dark)"/>
          <stop offset="1" stop-color="var(--band-light)"/>
        </linearGradient>
        <linearGradient id="band-bottom" x1="0" y1="1" x2="0" y2="0">
          <stop offset="0" stop-color="var(--band-dark)"/>
          <stop offset="1" stop-color="var(--band-light)"/>
        </linearGradient>
      </defs>
      <polygon class="band band--top" fill="url(#band-top)"
        points="0,0 864,0 864,96 574,96 556,117 308,117 290,96 0,96"/>
      <polygon class="band band--bottom" fill="url(#band-bottom)"
        points="0,432 864,432 864,336 574,336 556,317 308,317 290,336 0,336"/>
      <g class="rivets" fill="var(--rivet)" stroke="var(--rivet-edge)" stroke-width="1.5">
        <circle cx="349.5" cy="106" r="5"/>
        <circle cx="382.5" cy="106" r="5"/>
        <circle cx="415.5" cy="106" r="5"/>
        <circle cx="448.5" cy="106" r="5"/>
        <circle cx="481.5" cy="106" r="5"/>
        <circle cx="514.5" cy="106" r="5"/>
        <circle cx="349.5" cy="327" r="5"/>
        <circle cx="382.5" cy="327" r="5"/>
        <circle cx="415.5" cy="327" r="5"/>
        <circle cx="448.5" cy="327" r="5"/>
        <circle cx="481.5" cy="327" r="5"/>
        <circle cx="514.5" cy="327" r="5"/>
      </g>
    </svg>

    <div class="sign__phone">
      <span class="sign__phone-label">CALL/TEXT</span>
      <span class="sign__phone-number">555.382.4607</span>
    </div>

    <div class="sign__brand">
      <p class="sign__name">HAULPOINT GARAGE</p>
      <p class="sign__tagline">YOUR TRUSTED IRONLINE SPECIALISTS</p>
    </div>

    <div class="sign__web">WWW.HAULPOINTGARAGE-EXAMPLE.COM</div>
  </div>
</body>
</html>
```